Business Card Velostra - Accounting firm

Hi my friend.
I'm coming back to you to see if it would be possible for you to make a modern and minimalist business card design.
In shades of blue like the great logo you offered me.
The ideal is a modern and aesthetic business card.
The goal is to give a professional effect to the first exchanges.
Renewal and innovation in the accounting world !!
I thank you !!
Good evening to you

Target Market(s)

Young, dynamic and sensitive to marketing

Industry/Entity Type

Finance And Accounting

Contact Information for Business Card

Company logo and name. Last name, First name, Phone number, email address, company address, website.

Font styles to use
Sans Serif

Requirements
Must have
• The ideal is a modern and aesthetic business card.

Mentions to include: Company logo and name. Last name, First name, Phone number, email address, company address, website.
Nice to have
• The goal is to give a professional effect to the first exchanges.
Should not have
• Simplistic or childish design

```html
<!DOCTYPE html>
<html lang="en">
<head>
<meta charset="utf-8">
<title>Velostra – Business Card</title>
<link rel="stylesheet" href="https://fonts.googleapis.com/css2?family=Lato:wght@400;700&family=Montserrat:wght@700;800&display=swap">
<style>
  :root {
    --backdrop: #2a2b2e;
    --navy: #1f2c5f;
    --navy-deep: #1a2552;
    --pattern-light: #34406f;
    --white: #ffffff;
    --teal: #5fcdb0;
    --blue: #2a78d0;
    --divider: rgba(255,255,255,0.75);
  }
  * { box-sizing: border-box; margin: 0; padding: 0; }
  html, body { width: 1200px; height: 970px; overflow: hidden; }
  body {
    background: var(--backdrop);
    font-family: "Lato", sans-serif;
    color: var(--white);
    position: relative;
  }
  .card {
    position: absolute;
    width: 760px;
    height: 434px;
    background: var(--navy);
    overflow: hidden;
    box-shadow: 0 14px 30px rgba(0,0,0,0.45);
  }
  .card::after {
    content: "";
    position: absolute;
    left: 0; right: 0; bottom: 0;
    height: 7px;
    background: linear-gradient(90deg, var(--teal), var(--blue));
  }
  .card--front { left: 140px; top: 30px; }
  .card--back { left: 300px; top: 506px; }

  .pattern-field {
    position: absolute;
    left: 0; top: 0;
    width: 78%;
    height: 100%;
    background: linear-gradient(135deg, var(--pattern-light) 0%, var(--navy) 70%, var(--navy-deep) 100%);
    opacity: 0.8;
  }

  .brand { position: absolute; display: flex; flex-direction: column; align-items: flex-start; }
  .brand__name {
    font-family: "Montserrat", sans-serif;
    font-weight: 700;
    color: var(--white);
    line-height: 1;
    letter-spacing: -1px;
    display: flex;
    align-items: center;
  }
  .brand__mark {
    display: inline-block;
    background: var(--teal);
    border-radius: 4px;
    margin-right: 14px;
  }
  .brand__tagline {
    font-family: "Lato", sans-serif;
    letter-spacing: 6px;
    text-transform: uppercase;
  }

  .card--front .brand { right: 70px; top: 150px; }
  .card--front .brand__name { font-size: 58px; }
  .card--front .brand__mark { width: 40px; height: 40px; }
  .card--front .brand__tagline { font-size: 12px; margin: 6px 0 0 56px; }

  .card--back .brand { left: 180px; top: 70px; }
  .card--back .brand__name { font-size: 76px; }
  .card--back .brand__mark { width: 54px; height: 54px; }
  .card--back .brand__tagline { font-size: 15px; letter-spacing: 9px; margin: 8px 0 0 70px; }

  .person { position: absolute; left: 100px; top: 280px; text-align: right; width: 290px; }
  .person__name {
    font-family: "Montserrat", sans-serif;
    font-weight: 800;
    font-size: 34px;
    text-transform: uppercase;
  }
  .person__role { font-size: 22px; margin-top: 2px; }

  .divider {
    position: absolute;
    left: 420px; top: 240px;
    width: 1px; height: 130px;
    background: var(--divider);
  }

  .contact { position: absolute; left: 448px; top: 230px; list-style: none; font-size: 17px; line-height: 1.35; }
  .contact__address { margin-bottom: 8px; }
  .contact__row { display: flex; align-items: center; gap: 10px; }
  .contact__row svg { width: 16px; height: 16px; flex: none; }
</style>
</head>
<body>
  <section class="card card--front" aria-label="Card front">
    <div class="pattern-field" role="img" aria-label="Faint repeating brand motif pattern"></div>
    <div class="brand">
      <span class="brand__name"><span class="brand__mark"></span>velostra</span>
      <span class="brand__tagline">Expert-Comptable</span>
    </div>
  </section>

  <section class="card card--back" aria-label="Card back">
    <div class="brand">
      <span class="brand__name"><span class="brand__mark"></span>velostra</span>
      <span class="brand__tagline">Expert-Comptable</span>
    </div>

    <div class="person">
      <p class="person__name">John Smith</p>
      <p class="person__role">Founder &amp; CEO</p>
    </div>

    <div class="divider"></div>

    <ul class="contact">
      <li class="contact__address">1234 First Line Address<br>5678 Second Line Address</li>
      <li class="contact__row">
        <svg viewBox="0 0 24 24" fill="none" stroke="#fff" stroke-width="2"><path d="M5 3h4l2 5-3 2a12 12 0 0 0 6 6l2-3 5 2v4a2 2 0 0 1-2 2A17 17 0 0 1 3 5a2 2 0 0 1 2-2z"/></svg>
        1234567890
      </li>
      <li class="contact__row">
        <svg viewBox="0 0 24 24" fill="none" stroke="#fff" stroke-width="2"><rect x="3" y="5" width="18" height="14"/><path d="M3 5l9 8 9-8"/></svg>
        info@yourmail.com
      </li>
      <li class="contact__row">
        <svg viewBox="0 0 24 24" fill="none" stroke="#fff" stroke-width="2"><circle cx="12" cy="12" r="9"/><path d="M3 12h18M12 3c3 3 3 15 0 18M12 3c-3 3-3 15 0 18"/></svg>
        www.yourwebsite.com
      </li>
    </ul>
  </section>
</body>
</html>
```